Coffee Bag Label design for Australian Firefighter brand

I need a label for coffee bags. Front and back. We are based in Australia and aimed at Firefighters and First responders. I will have three size available. 250g, 500g and 1kg. So if we can use the same label that would be great. maybe a check box option at the bottom with the three sizes.
I really like the design for Lanternfield Coffee (see attached), so I'm hoping for something along the same lines. replacing the images with firefighter axe, hose, halagan tool, cutting gear etc
I would like to include 'Firefighter founded" on the front, as well as 'Quarry Gate Blend'. Roasted med-dark on the Sunshine Coast, QLD
On the back I need space for a qr code with an arrow pointing to it with handwritten font 'how're you travelling? Free, confidential wellness check in'
and the text;
Coffee without the b.s.
This ain’t the sort of coffee for your average piccolo drinking, man-bun enthusiast. No fancy rose petal and unicorn pube infusions here. Just consistently great coffee that shows up, for those who show up. Firefighter founded and built with the Australian First Responder in mind.
Your life is complicated enough. Your coffee shouldn’t be.
For more, go to brasskettleroast.com.au or scan the QR code for a free, fast, confidential mental wellness check-in and useful resources.
These will be printed as sticker lables to go on kraft black coffee bags to begin with. Please see attached bag example and logo for use.
Target Market(s)
Australian Firefighters and First responders
Look and feel
Each slider illustrates characteristics of the customer's brand and the style your logo design should communicate.

```html
<!DOCTYPE html>
<html lang="en">
<head>
<meta charset="utf-8">
<title>Coffee Without the B.S. — Back Label</title>
<link rel="stylesheet" href="https://fonts.googleapis.com/css2?family=Oswald:wght@300;400;700&display=swap">
<style>
  :root {
    --bg: #3b3f40;
    --red-title: #d33b48;
    --red-frame: #e8433a;
    --red-note: #e5414c;
    --white: #f1f1f1;
    --art-tone: #c9c9c9;
  }
  html, body {
    margin: 0;
    padding: 0;
    overflow: hidden;
    background: var(--bg);
  }
  .label {
    position: relative;
    width: 1043px;
    height: 1200px;
    background: var(--bg);
    overflow: hidden;
    font-family: "Oswald", "Arial Narrow", sans-serif;
    color: var(--white);
  }
  .headline {
    position: absolute;
    left: 86px;
    top: 62px;
    margin: 0;
    font-weight: 700;
    font-size: 132px;
    line-height: 1;
    color: var(--red-title);
    letter-spacing: 1px;
  }
  .subhead {
    position: absolute;
    left: 88px;
    top: 202px;
    margin: 0;
    font-weight: 700;
    font-size: 68px;
    line-height: 1;
    color: var(--white);
    letter-spacing: 1px;
  }
  .story-frame {
    position: absolute;
    left: 84px;
    top: 305px;
    width: 482px;
    height: 613px;
    box-sizing: border-box;
    border: 7px solid var(--red-frame);
    border-radius: 46px;
  }
  .story {
    position: absolute;
    left: 146px;
    top: 348px;
    width: 350px;
    margin: 0;
    font-weight: 300;
    font-size: 19.5px;
    line-height: 27px;
    color: var(--white);
  }
  .art-extinguisher {
    position: absolute;
    left: 640px;
    top: 89px;
    width: 346px;
    height: 650px;
    background: linear-gradient(180deg, rgba(230,230,230,0.28), rgba(200,200,200,0.18));
    border-radius: 40px 40px 10px 10px;
  }
  .art-axe {
    position: absolute;
    left: 300px;
    top: 930px;
    width: 560px;
    height: 110px;
    background: linear-gradient(90deg, rgba(230,230,230,0.3), rgba(200,200,200,0.16));
    transform: rotate(22deg);
    transform-origin: left center;
    border-radius: 14px;
  }
  .pointer-arrow {
    position: absolute;
    left: 350px;
    top: 700px;
    width: 300px;
    height: 150px;
  }
  .callout-lead {
    position: absolute;
    left: 696px;
    top: 770px;
    margin: 0;
    font-weight: 700;
    font-size: 47px;
    line-height: 1;
    color: var(--white);
  }
  .callout-main {
    position: absolute;
    left: 694px;
    top: 812px;
    margin: 0;
    font-weight: 700;
    font-size: 96px;
    line-height: 1;
    color: var(--white);
  }
  .callout-note {
    position: absolute;
    left: 697px;
    top: 918px;
    width: 230px;
    margin: 0;
    font-weight: 700;
    font-size: 20px;
    line-height: 26px;
    color: var(--red-note);
  }
  .address {
    position: absolute;
    left: 88px;
    top: 1062px;
    margin: 0;
    font-weight: 300;
    font-size: 29px;
    line-height: 36px;
    color: var(--white);
    font-style: normal;
  }
</style>
</head>
<body>
  <main class="label">
    <div class="art-extinguisher" role="img" aria-label="Illustration of a fire extinguisher in white sketch style"></div>

    <h1 class="headline">COFFEE</h1>
    <h2 class="subhead">WITHOUT THE B.S.</h2>

    <div class="story-frame"></div>
    <p class="story">This ain’t the sort of coffee for your average piccolo drinking, man-bun enthusiast. No fancy rose petal and unicorn pube infusions here. Just consistently great coffee that shows up, for those who show up.<br>Firefighter founded and built with the Australian First Responder in mind. Your life is complicated enough. Your coffee shouldn’t be.</p>

    <svg class="pointer-arrow" viewBox="0 0 300 150" aria-hidden="true">
      <path d="M8 12 C60 -4 120 20 70 44 C30 62 20 30 60 24 C120 16 200 40 262 96"
            fill="none" stroke="var(--white)" stroke-width="6" stroke-linecap="round"/>
      <path d="M228 92 L268 104 L256 62" fill="none" stroke="var(--white)" stroke-width="6" stroke-linecap="round" stroke-linejoin="round"/>
    </svg>

    <div class="art-axe" role="img" aria-label="Illustration of a firefighter axe in white sketch style"></div>

    <p class="callout-lead">FIT FOR OFF</p>
    <p class="callout-main">DUTY</p>
    <p class="callout-note">Scan here for free firefighter wellness resources.</p>

    <address class="address">27 Marlow ave,<br>Witta, QLD</address>
  </main>
</body>
</html>
```